Mt Korrow - Outback Australia (Working farm, film location and farmstay promotation)

I need a website to promote my film location and farm stay business. Would like the ability to have online booking also and payment options

REFER TO
https://rs.scenevaultr.net/location_detail.aspx?id=052-48213906&search=broken%20hill&search_mode=and&ctry=all&state=&city=&cat=&subcat=&style=&lname=&locid=&int=&parent=search_results

https://www.pagelinkr.net/pg/mountkorrowstation/photos/?ref=page_internal

Target Market(s)

International Tourists
Film crews

Coding

Coded - Design and coding required

Number of Pages Required

1 page

Colors

Designer to choose colors to be used in the design.

Requirements
Must have
• Ability for online booking

```html
<!DOCTYPE html>
<html lang="en">
<head>
<meta charset="utf-8">
<title>Mt Korrow Station Stay</title>
<link href="https://fonts.googleapis.com/css2?family=Poppins:wght@300;400;500;600&display=swap" rel="stylesheet">
<style>
:root{
  --orange:#f9640a;
  --yellow:#f7d038;
  --ink:#1d1d1d;
  --muted:#777;
  --dark:#1b1b1b;
  --line:#e3e3e3;
  --white:#fff;
}
*{margin:0;padding:0;box-sizing:border-box}
html,body{width:1200px;height:2837px;overflow:hidden;background:var(--white)}
body{position:relative;font-family:'Poppins',sans-serif;color:var(--ink)}
.abs{position:absolute}
.accent{color:var(--orange)}
.btn-solid{position:absolute;background:var(--orange);color:#fff;border-radius:18px;font-size:11px;font-weight:600;display:flex;align-items:center;justify-content:center}
.btn-line{position:absolute;border:2px solid var(--orange);border-radius:18px;font-size:11px;font-weight:600;display:flex;align-items:center;justify-content:center}
.section-title{position:absolute;font-size:29px;font-weight:400;width:100%;text-align:center}

/* header */
.brand{left:88px;top:44px;display:flex;align-items:center;gap:10px}
.brand-dot{width:34px;height:34px;border-radius:50%;background:var(--yellow)}
.brand-name{font-size:22px;font-weight:600;color:var(--orange)}
.call{left:750px;top:33px;font-size:14px;font-weight:500}
.nav{top:82px;left:0;width:1200px;font-size:12px}
.nav span{position:absolute}

/* hero */
.hero{left:0;top:120px;width:1200px;height:520px;background:linear-gradient(180deg,#6b6e73 0%,#8a8580 40%,#7a5a45 75%,#4a3628 100%)}
.hero-title{left:88px;top:292px;font-size:28px;line-height:34px;color:#fff;font-weight:300}
.hero-title b{font-weight:600}
.booking{left:616px;top:236px;width:496px;height:286px;background:#fafafa}
.booking h2{position:absolute;left:32px;top:24px;font-size:24px;font-weight:400}
.booking p{position:absolute;left:32px;top:58px;font-size:13px;color:var(--muted)}
.field{position:absolute;width:210px;height:32px;border-radius:16px;background:#fff;box-shadow:0 1px 4px rgba(0,0,0,.08);font-size:11px;color:#aaa;padding:9px 16px}

/* services */
.services{left:0;top:640px;width:1200px;height:488px;background:var(--yellow)}
.service{position:absolute;width:320px;text-align:center}
.service-photo{width:164px;height:164px;border-radius:50%;margin:0 auto;overflow:hidden;position:relative}
.service h3{font-size:17px;font-weight:600;margin-top:26px}
.service p{font-size:13px;line-height:18px;margin-top:12px;color:#6b5e22}
.service.first p{color:var(--ink)}

/* about */
.about-title{left:88px;top:1240px;font-size:29px;font-weight:400}
.about-text{left:88px;top:1294px;width:480px;font-size:15px;line-height:24px;color:#333}
.about-text b{font-weight:500;color:var(--ink)}
.weather{left:616px;top:1208px;width:496px;height:287px;background:#f2f2f2}
.weather-card{position:absolute;left:32px;top:37px;width:432px;height:218px;background:#fff}

/* gallery */
.thumb{position:absolute;top:1932px;width:160px;height:160px}

/* footer */
.footer{left:0;top:2172px;width:1200px;height:665px;background:var(--dark);color:#ccc}
.social{position:absolute;top:366px;width:30px;height:30px;border:1.5px solid var(--orange);border-radius:50%}
</style>
</head>
<body>

<!-- header -->
<div class="abs brand"><div class="brand-dot"></div><div class="brand-name">Mt Korrow</div></div>
<div class="abs call"><span class="accent">Call Us:</span>
 <svg width="14" height="14" viewBox="0 0 24 24" style="vertical-align:-2px"><path d="M6 2l4 4-2 3c1 3 4 6 7 7l3-2 4 4-3 4C10 22 2 14 2 5z" fill="none" stroke="#f9640a" stroke-width="2"/></svg>
 +61 2 8374 5190</div>
<div class="btn-solid" style="left:984px;top:28px;width:127px;height:30px">Book Now!</div>
<nav class="abs nav">
 <span class="accent" style="left:472px">Home</span>
 <span style="left:574px">About Us</span>
 <span style="left:695px">Services</span>
 <span style="left:812px">Gallery</span>
 <span style="left:921px">Location</span>
 <span style="left:1039px">Contact Us</span>
</nav>

<!-- hero -->
<div class="abs hero" role="img" aria-label="Photo of the station homestead veranda under a cloudy outback sky"></div>
<h1 class="abs hero-title">Contrary to <b>Popular work</b><br>Belief, Lorem Ipsum classical<br><b>randomised</b> words!</h1>
<div class="btn-line" style="left:88px;top:429px;width:128px;height:31px;color:#fff">Contact Us</div>
<form class="abs booking">
 <h2>Check <span class="accent">Available Dates</span></h2>
 <p>Please choose an arrival and departure date</p>
 <div class="field" style="left:30px;top:114px">Arrival Date</div>
 <div class="field" style="left:253px;top:114px">Departure Date</div>
 <div class="field" style="left:30px;top:162px">Adults</div>
 <div class="field" style="left:253px;top:162px">Children</div>
 <div class="btn-solid" style="left:31px;top:211px;width:432px;height:31px">Check Availability</div>
</form>

<!-- services -->
<section class="abs services">
 <h2 class="section-title" style="top:73px">Our <span class="accent">Services</span></h2>
 <div class="service first" style="left:88px;top:142px">
  <div class="service-photo" role="img" aria-label="Photo of a cosy living room" style="background:linear-gradient(160deg,#d9d2c8,#8b6f55)"></div>
  <h3>Accommodation</h3>
  <p>Lorem Ipsum is simply dummy text of<br>printing and typesetting industry. Lorem Ipsum<br>has been industry's standard.</p>
 </div>
 <div class="service" style="left:440px;top:142px">
  <div class="service-photo" role="img" aria-label="Photo of a breakfast table" style="background:linear-gradient(160deg,#e9e3de,#b34a3e)"></div>
  <h3>Dining</h3>
  <p>Lorem Ipsum is simply dummy text of<br>printing and typesetting industry. Lorem Ipsum<br>has been industry's standard.</p>
 </div>
 <div class="service" style="left:792px;top:142px">
  <div class="service-photo" role="img" aria-label="Photo of a tent at sunset" style="background:linear-gradient(180deg,#3a4250,#a35f2e 70%,#5a3a22)"></div>
  <h3>Caravan and Camp</h3>
  <p>Lorem Ipsum is simply dummy text of<br>printing and typesetting industry. Lorem Ipsum<br>has been industry's standard.</p>
 </div>
 <svg class="abs" style="left:0;top:0" width="1200" height="488">
  <g fill="#000">
   <path d="M126 276 Q248 214 370 276 Q248 234 126 276Z"/><path d="M185 254 Q248 234 311 254 A82 82 0 0 1 185 254Z"/>
   <path d="M478 276 Q600 214 722 276 Q600 234 478 276Z"/><path d="M537 254 Q600 234 663 254 A82 82 0 0 1 537 254Z"/>
   <path d="M830 276 Q952 214 1074 276 Q952 234 830 276Z"/><path d="M889 254 Q952 234 1015 254 A82 82 0 0 1 889 254Z"/>
  </g>
  <g fill="none" stroke="#f7d038" stroke-width="2.4">
   <rect x="235" y="265" width="28" height="18" rx="3"/><path d="M235 275h28M241 265v-3h16v3"/>
   <path d="M592 262v22M588 262v8q4 4 8 0v-8M609 262q-6 4-4 12h4v10"/>
   <path d="M940 283v-12l12-9 12 9v12zM947 283v-7h10v7"/>
  </g>
 </svg>
</section>

<!-- about -->
<h2 class="abs about-title">About <span class="accent">Mt Korrow</span></h2>
<p class="abs about-text"><b>Mt Korrow Station is an 85,000 acre sheep</b> and<br>cattle property about 40kms/30 minute drive north of the<br>regional city en Hill. Features include hills, gorges,<br>mines, rock formations and creeks.</p>
<div class="btn-line" style="left:88px;top:1422px;width:128px;height:31px">Book Now!</div>
<div class="abs weather">
 <div class="weather-card">
  <div class="abs" style="left:25px;top:18px;font-size:13px;font-weight:500">Weather for Dunmarra Flat</div>
  <div class="abs" style="left:322px;top:22px;font-size:10px;color:#666">More at <u>SkyCast</u></div>
  <div class="abs" style="left:20px;top:38px;width:400px;height:2px;background:#333"></div>
  <svg class="abs" style="left:33px;top:75px" width="34" height="34"><circle cx="17" cy="17" r="13" fill="none" stroke="#333" stroke-width="5" stroke-dasharray="60 30"/></svg>
  <div class="abs" style="left:92px;top:62px;font-size:34px;font-weight:600">25°</div>
  <div class="abs" style="left:93px;top:100px;font-size:10px;color:#666">and falling</div>
  <div class="abs" style="left:70px;top:130px;font-size:12px;font-weight:500">Clear</div>
  <div class="abs" style="left:37px;top:147px;font-size:10px;color:#666">Wind: 20 km/h (NW)</div>
  <svg class="abs" style="left:160px;top:50px" width="270" height="160" font-family="Poppins,sans-serif" font-size="9" text-anchor="middle" fill="#333">
   <g><text x="15" y="9">Today</text><text x="47" y="9">Tue</text><text x="79" y="9">Wed</text><text x="111" y="9">Thu</text><text x="141" y="9">Fri</text><text x="171" y="9">Sat</text><text x="201" y="9">Sun</text><text x="233" y="9">Mon</text></g>
   <g fill="none" stroke="#333"><circle cx="15" cy="25" r="4"/><circle cx="47" cy="25" r="4"/><circle cx="79" cy="25" r="4"/><circle cx="111" cy="25" r="4"/><circle cx="141" cy="25" r="4"/><circle cx="171" cy="25" r="4"/><circle cx="201" cy="25" r="4"/><circle cx="233" cy="25" r="4"/></g>
   <g fill="#222"><rect x="8" y="57" width="14" height="46" rx="7"/><rect x="40" y="74" width="14" height="26" rx="7"/><rect x="72" y="79" width="14" height="34" rx="7"/><rect x="104" y="68" width="14" height="36" rx="7"/><rect x="134" y="61" width="14" height="42" rx="7"/><rect x="164" y="64" width="14" height="39" rx="7"/><rect x="194" y="58" width="14" height="46" rx="7"/><rect x="226" y="44" width="14" height="44" rx="7"/></g>
   <g font-size="8"><text x="15" y="52">32°</text><text x="47" y="70">24°</text><text x="79" y="75">23°</text><text x="111" y="64">26°</text><text x="141" y="57">29°</text><text x="171" y="60">27°</text><text x="201" y="54">30°</text><text x="233" y="40">35°</text>
   <text x="15" y="113">13°</text><text x="47" y="110">14°</text><text x="79" y="123">8°</text><text x="111" y="114">11°</text><text x="141" y="113">13°</text><text x="171" y="113">13°</text><text x="201" y="114">14°</text><text x="233" y="98">17°</text></g>
  </svg>
 </div>
</div>

<!-- gallery -->
<h2 class="section-title" style="top:1567px">Photo <span class="accent">Gallery</span></h2>
<div class="abs" role="img" aria-label="Photo of the homestead on red outback earth" style="left:168px;top:1638px;width:864px;height:279px;background:linear-gradient(180deg,#8d98a2 0%,#b9bcbc 45%,#8c5a3e 70%,#7a4630 100%)"></div>
<div class="thumb" role="img" aria-label="Photo of a weatherboard cottage" style="left:168px;background:linear-gradient(180deg,#a8b4c0,#6d6a5c)"></div>
<div class="thumb" role="img" aria-label="Photo of rock formations" style="left:343px;background:linear-gradient(180deg,#c9ccd0,#6d4a3c)"></div>
<div class="thumb" role="img" aria-label="Photo of a dust storm over the plains" style="left:519px;background:linear-gradient(180deg,#e6874b,#c5582a)"></div>
<div class="thumb" role="img" aria-label="Photo of a hut on the plains" style="left:694px;background:linear-gradient(180deg,#9aa0a8,#7a6350)"></div>
<div class="thumb" role="img" aria-label="Photo of a creek bed" style="left:871px;background:linear-gradient(180deg,#9ba6b2,#8a5b44)"></div>
<svg class="abs" style="left:118px;top:1998px" width="14" height="26"><path d="M11 3L3 13l8 10" fill="none" stroke="#777" stroke-width="1.5"/></svg>
<svg class="abs" style="left:1066px;top:1998px" width="14" height="26"><path d="M3 3l8 10-8 10" fill="none" stroke="#777" stroke-width="1.5"/></svg>

<!-- footer -->
<footer class="abs footer">
 <h2 class="abs" style="left:88px;top:68px;font-size:24px;font-weight:400;color:#fff">Contact <span class="accent">Us</span></h2>
 <div class="abs" style="left:88px;top:124px;font-size:13px;line-height:18px">
  <div class="accent" style="font-weight:500">Mount Korrow Station</div>
  <div>Dunmarra Flat, NSW 2881</div>
  <div class="accent" style="margin-top:16px;font-weight:500">CALL: +61 2 8374 5190</div>
  <div>E. info@mountkorrowstation.com</div>
 </div>
 <div class="btn-solid" style="left:88px;top:272px;width:128px;height:31px">Book Now!</div>
 <a class="social" style="left:88px" aria-label="Social page"></a>
 <a class="social" style="left:127px" aria-label="Photo page"></a>
 <div class="abs" role="img" aria-label="Map showing the station location" style="left:432px;top:80px;width:680px;height:320px;background:#ededed"></div>
 <p class="abs" style="left:88px;top:496px;width:1024px;font-size:11px;line-height:17px;color:#bbb"><span class="accent" style="font-weight:600">Disclaimer:</span> All data, information, and maps are provided "as is" without warranty or any representation of accuracy, timeliness or completeness. The content of the information is solely dependent on the location owner/contact and no warranties, express or implied, as to the use of the information are obtained here. The requestor acknowledges and accepts all limitations, including the fact that the data, information, and maps are dynamic and in a constant state of maintenance, correction and update.</p>
 <div class="abs" style="left:88px;top:590px;width:1024px;height:1px;background:#3a3a3a"></div>
 <div class="abs" style="left:88px;top:621px;font-size:11px">© 2019 <span class="accent">Mount Korrow Station</span>. All Right Reserved</div>
 <svg class="abs" style="left:1094px;top:618px" width="16" height="18"><path d="M8 2L2 16M8 2l6 14M4 11h8" fill="none" stroke="#f9640a" stroke-width="2"/></svg>
</footer>

</body>
</html>
```